FItness Bootcamp Flyer

We need an A4 flyer to distribute on an advertising board, and also distribute in the mail.

It should contain a photo(s) of females exercising and having fun outdoors.

It should contain the following text and if you think it could be worded better please change as I'm just looking at getting people to come along:

- KestrelMove Studio Outdoor Bootcamp
Get moving, get fit and feel great

Commencing 19th May

Get results before the winter season
6 Week Bootcamp for $49. Limited numbers!
Or casual visit $10 per session

Now is the time to:
- Lose Weight and Tone-up
- Build Strength and Endurance
- Increase Cardio Fitness
- Improve Your Energy and Vitality
- Fun Varied and Exciting Training Programs
- ALL Fitness Levels

LADIES ONLY BOOTCAMP SUBIACO
Monday 6:30-7:15am, 8:30-9:15am
Wednesday 6:30-7:!5am, 8:30-9:15am
Friday 8:30-9:15am,

Register you place now on 0428 574 812 or email: kestrelmovestudio@fernmail.net

facebook.com/KestrelMove Studio

Target Market(s)

Females 20-60yrs

Industry/Entity Type

Advertising

Requirements
Nice to have
• - We like the words and style of the Harbourline Open Air Training flyer attached
- Also the Vanta Group brochure
- I like the colour Blue, Green, Pink. They don't all have to be used but at least one would be nice thank you

```html
<!DOCTYPE html>
<html lang="en">
<head>
<meta charset="utf-8">
<title>KestrelMove Studio – Outdoor Bootcamp</title>
<link href="https://fonts.googleapis.com/css2?family=Arimo:ital,wght@0,400;0,700;1,400&family=Lobster&family=Questrial&display=swap" rel="stylesheet">
<style>
:root{
  --pink:#ec4679;
  --pink-soft:#f48fb1;
  --teal:#1c9ab2;
  --teal-text:#17959e;
  --maroon:#7e1b1f;
  --wood:#8a3f1f;
  --cream:#f6dfc0;
  --green-day:#4cc98e;
  --orange-day:#f57f5b;
  --aqua-day:#72c4bb;
  --ink:#222;
  --white:#fff;
}
*{margin:0;padding:0;box-sizing:border-box}
html,body{width:848px;height:1200px;overflow:hidden;background:#fff}
.flyer{position:relative;width:848px;height:1200px;overflow:hidden;font-family:"Questrial",sans-serif;color:var(--ink)}
.abs{position:absolute}
.hero-photo{left:0;top:0;width:848px;height:1200px;
  background:linear-gradient(180deg,#c9d3d6 0%,#9fb3b8 9%,#7f9b5a 20%,#86a83e 40%,#8ba52a 70%,#98ac1e 100%)}
.brand{left:0;top:78px;width:848px;text-align:center;font-family:"Arimo",sans-serif;font-weight:700;font-size:66px;color:var(--pink);letter-spacing:1px}
.snap{border:5px solid var(--maroon);background:linear-gradient(160deg,#b9cbd0 0%,#8fb35a 45%,#6f9a34 100%)}
.snap-1{left:301px;top:258px;width:198px;height:160px;transform:rotate(-8deg)}
.snap-2{left:447px;top:250px;width:190px;height:158px;transform:rotate(-6deg)}
.snap-3{left:588px;top:248px;width:180px;height:142px;transform:rotate(-8deg)}
.sign{left:84px;top:218px;width:310px;height:168px;background:var(--wood);border-radius:6px;transform:rotate(-10deg);
  display:flex;flex-direction:column;justify-content:center;align-items:center;box-shadow:0 3px 6px rgba(0,0,0,.35)}
.sign span{font-family:"Lobster",cursive;color:var(--cream);font-size:54px;line-height:58px}
.panel{left:38px;top:386px;width:772px;height:814px;background:var(--white);border:3px solid var(--maroon);border-bottom:none;border-radius:10px 10px 0 0;overflow:hidden}
.panel-head{left:0;top:0;width:100%;height:78px;background:var(--teal)}
.tagline{left:38px;top:410px;width:772px;text-align:center;font-family:"Arimo",sans-serif;font-style:italic;font-size:30px;color:var(--white)}
.benefits-title{left:75px;top:488px;font-size:33px;font-weight:400;color:var(--teal-text)}
.benefits{left:75px;top:530px;list-style:none;font-size:25px;line-height:35.6px}
.divider{left:388px;top:488px;height:398px;border-left:2px dashed #555}
.figure{left:612px;top:548px;width:150px;height:340px;background:var(--pink-soft);opacity:.6;border-radius:70px 70px 12px 12px}
.ribbon{left:412px;top:484px;width:420px;height:60px}
.ribbon-text{left:430px;top:488px;width:400px;text-align:center;font-size:31px;color:var(--white)}
.day{left:449px;width:179px;height:99px;border-radius:14px;text-align:center;color:var(--white)}
.day h3{font-weight:400;font-size:21px;color:#333;padding-top:8px;margin:0 14px;border-bottom:1.5px solid var(--white);padding-bottom:3px}
.day p{font-family:"Arimo",sans-serif;font-size:16px;line-height:26px;margin-top:5px}
.day-mon{top:551px;background:var(--green-day)}
.day-wed{top:667px;background:var(--orange-day)}
.day-fri{top:787px;background:var(--aqua-day)}
.day-fri p{margin-top:12px}
.ladies{left:560px;top:707px;width:310px;transform:rotate(-90deg);text-align:center;font-family:"Arimo",sans-serif;font-size:23px;line-height:26px;color:#333}
.offer{left:19px;top:901px;width:808px;height:144px;background:var(--pink)}
.offer-text{left:84px;top:918px;font-family:"Arimo",sans-serif;font-size:29px;line-height:34.5px;color:var(--white)}
.offer-text b{font-weight:700}
.offer-text .script{font-family:"Lobster",cursive;font-weight:400}
.register{left:113px;top:1078px;font-size:29px;line-height:36px;color:#111;white-space:nowrap}
.register-line{left:361px;top:1078px;height:38px;border-left:2px solid #111}
.contact{left:371px;top:1072px;font-size:20px;line-height:24px;color:#111;white-space:nowrap}
.footer{left:38px;top:1143px;width:772px;height:57px;background:var(--teal)}
.footer-text{left:38px;top:1160px;width:772px;text-align:center;font-size:20px;color:#333}
</style>
</head>
<body>
<main class="flyer">
  <div class="abs hero-photo" role="img" aria-label="Photo of women exercising on a grassy foreshore beside a jetty and the water"></div>
  <h1 class="abs brand">KestrelMove Studio</h1>

  <div class="abs snap snap-1" role="img" aria-label="Photo of a woman doing push-ups on a path"></div>
  <div class="abs snap snap-2" role="img" aria-label="Photo of a woman lifting a kettlebell on an exercise ball"></div>
  <div class="abs snap snap-3" role="img" aria-label="Photo of a woman training beside yellow hurdles"></div>

  <div class="abs sign"><span>Outdoor</span><span>Bootcamp</span></div>

  <section class="abs panel"><div class="abs panel-head"></div></section>
  <p class="abs tagline">Get moving, get fit and feel great!!!</p>

  <div class="abs figure" role="img" aria-label="Pink silhouette of a woman lifting a dumbbell"></div>

  <h2 class="abs benefits-title">Now is the time to:</h2>
  <ul class="abs benefits">
    <li>- Lose Weight<br>&nbsp;&nbsp;and Tone-up</li>
    <li>- Build Strength<br>&nbsp;&nbsp;and Endurance</li>
    <li>- Increase Cardio Fitness</li>
    <li>- Improve Your Energy<br>&nbsp;&nbsp;and Vitality</li>
    <li>- Fun Varied and Exciting<br>&nbsp;&nbsp;Training Programs</li>
    <li>- ALL Fitness Levels</li>
  </ul>
  <div class="abs divider"></div>

  <svg class="abs ribbon" viewBox="0 0 420 60" aria-hidden="true">
    <polygon points="0,2 398,2 398,46 0,46 24,24" fill="var(--pink)"/>
    <polygon points="398,46 412,46 398,58" fill="var(--maroon)"/>
  </svg>
  <p class="abs ribbon-text">Commencing 19th May</p>

  <div class="abs day day-mon"><h3>Monday</h3><p>6:30-7:15am<br>8:30-9:15am</p></div>
  <div class="abs day day-wed"><h3>Wednesday</h3><p>6:30-7:15am<br>8:30-9:15am</p></div>
  <div class="abs day day-fri"><h3>Friday</h3><p>8:30-9:15am</p></div>

  <p class="abs ladies">LADIES ONLY BOOTCAMP<br>SUBIACO</p>

  <div class="abs offer"></div>
  <p class="abs offer-text">
    <b>Get results before the winter season</b>.<br>
    <span class="script">Six Week Bootcamp</span> for <b>$49</b>. <i>Limited numbers</i>!<br>
    Or <span class="script">casual visit</span> for <b>$10</b> per session.
  </p>

  <p class="abs register">REGISTER NOW</p>
  <div class="abs register-line"></div>
  <p class="abs contact">contact: 0428 574 812<br>email: kestrelmovestudio@fernmail.net</p>

  <div class="abs footer"></div>
  <p class="abs footer-text">facebook.com/KestrelMoveStudio</p>
</main>
</body>
</html>
```